Powerpoint Sales and Pre-Sales Decks

We need a GD to support us as we start buillidng many PPT decks - we are a start-up based in London in the Telecomms space

```html
<!DOCTYPE html>
<html lang="en">
<head>
<meta charset="utf-8">
<title>Telecom Sales Deck – Slide Overview</title>
<link href="https://fonts.googleapis.com/css2?family=Open+Sans:wght@300;400;600;700&display=swap" rel="stylesheet">
<style>
:root{
  --stage-light:#d4d4d4;
  --stage-dark:#8c8c8c;
  --navy:#0b2470;
  --navy-deep:#0a2a78;
  --title-blue:#1aa3e0;
  --bright-blue:#08a0ec;
  --mid-blue:#0a7fd8;
  --text-gray:#555a60;
  --white:#ffffff;
}
*{box-sizing:border-box;margin:0;padding:0}
html,body{width:1200px;height:900px;overflow:hidden}
body{
  font-family:"Open Sans",sans-serif;
  background:radial-gradient(ellipse at 50% 45%,var(--stage-light) 0%,#b3b3b3 60%,var(--stage-dark) 100%);
  position:relative;
}
h2,h3{font-weight:400}
.slide{position:absolute;width:378px;height:212px;overflow:hidden;background:var(--white)}
.col-1{left:28px}.col-2{left:411px}.col-3{left:794px}
.row-1{top:17px}.row-2{top:235px}.row-3{top:453px}.row-4{top:671px}
.abs{position:absolute}
.slide-title{position:absolute;left:18px;top:14px;font-size:12.5px;font-weight:400;color:var(--title-blue);line-height:1.2}
.slide-title.on-dark{color:var(--white);font-weight:400}
.logo-box{position:absolute;right:18px;bottom:8px;width:37px;height:12px;background:var(--navy);color:var(--white);font-size:4.2px;display:flex;align-items:center;justify-content:center;white-space:nowrap}
.page-no{position:absolute;left:18px;bottom:10px;font-size:3.5px;color:#999}
.fine{font-size:5px;line-height:1.35;color:var(--text-gray)}
.photo-fill{position:absolute;inset:0}
.welcome-bg{background:radial-gradient(ellipse at 50% 30%,#4a5178 0%,#3a4064 55%,#2f3454 100%)}
.welcome-text{position:absolute;left:0;right:0;top:100px;text-align:center;color:var(--white);font-size:9px;font-weight:300}
.welcome-logo{position:absolute;left:154px;top:116px;width:70px;height:12px;border:0.8px solid #e0e0ee;color:var(--white);font-size:6px;display:flex;align-items:center;justify-content:center}
.cover-bg{background:linear-gradient(120deg,#9c9ed8 0%,#a9a6e2 35%,#7d7ccd 65%,#5a5fb6 100%)}
.cover-logo{position:absolute;left:14px;top:15px;width:36px;height:11px;background:var(--navy);color:var(--white);font-size:4px;display:flex;align-items:center;justify-content:center}
.cover-title{position:absolute;left:14px;top:118px;color:var(--white);font-size:13px;font-weight:300;line-height:1.25}
.cover-sub{position:absolute;left:14px;top:169px;color:var(--white);font-size:6.5px;font-weight:300}
.cover-date{position:absolute;left:14px;top:188px;color:var(--white);font-size:5.5px;font-weight:300}
.bullet-box{position:absolute;left:39px;top:73px;width:301px;height:86px;border:0.7px solid #9a9a9a;padding:3px 6px 0 10px}
.bullet-box ul{list-style:none}
.bullet-box li{font-size:5px;line-height:1.46;color:#333;position:relative}
.bullet-box li::before{content:"•";position:absolute;left:-7px}
.bullet-box b{color:#222}
.hl-light{color:var(--title-blue)}
.hl-bold{color:var(--title-blue);font-weight:700}
.agenda-item{position:absolute;width:108px}
.agenda-item.active{color:var(--title-blue)}
.section-bg{background:radial-gradient(ellipse at 35% 35%,#1e4aa8 0%,#0e3592 45%,#0a2878 100%)}
.section-title{position:absolute;left:0;right:0;top:96px;text-align:center;color:var(--white);font-size:16px;font-weight:300}
.impact-bg{background:linear-gradient(180deg,var(--bright-blue) 0%,#0892e6 55%,#0a6fd3 100%)}
.stat{position:absolute;color:var(--white)}
.stat-value{font-size:17px;font-weight:300;line-height:1}
.stat-text{font-size:5px;line-height:1.35;margin-top:5px;width:72px}
.laptop-screen{position:absolute;left:180px;top:42px;width:198px;height:142px;border:4px solid #d9d3c6;border-radius:4px;background:linear-gradient(160deg,#5e86b8 0%,#8fb0d6 45%,#3d5f98 100%)}
.laptop-base{position:absolute;left:146px;top:185px;width:232px;height:6px;background:#cfc8b8;border-radius:0 0 3px 3px}
.portfolio-title{position:absolute;left:18px;top:86px;font-size:12.5px;font-weight:400;color:var(--title-blue);line-height:1.25}
.portfolio-text{position:absolute;left:18px;top:124px;font-size:7px;line-height:1.35;color:#444}
.node-label{position:absolute;width:52px;text-align:center;font-size:4.2px;line-height:1.3;color:var(--text-gray)}
.growth-text{position:absolute;left:18px;top:111px;width:100px;font-size:7px;line-height:1.5;color:#7a7f86}
.step-label{position:absolute;width:40px;text-align:center;font-size:4.6px;line-height:1.25;color:#444}
.services-bg{background:var(--bright-blue)}
.service{position:absolute;color:var(--white);width:90px}
.service h3{font-size:7px;font-weight:400;letter-spacing:0.2px}
.service p{font-size:5px;line-height:1.35;margin-top:3px}
</style>
</head>
<body>

<section class="slide col-1 row-1">
  <div class="photo-fill welcome-bg" role="img" aria-label="Night city aerial with connection arcs linking points"></div>
  <div class="welcome-text">Welcome</div>
  <div class="welcome-logo">Your logo here</div>
</section>

<section class="slide col-2 row-1">
  <div class="photo-fill cover-bg" role="img" aria-label="Satellite dish in front of a blurred city skyline at dusk"></div>
  <div class="cover-logo">Your logo here</div>
  <div class="cover-title">Enter your<br>Presentation title here</div>
  <div class="cover-sub">Sub title here</div>
  <div class="cover-date">Date here</div>
</section>

<section class="slide col-3 row-1">
  <h2 class="slide-title">Slide title here in this color and format</h2>
  <div class="bullet-box">
    <ul>
      <li>This is a generic slide template. This is the basic slide with title and running content</li>
      <li>The company logo is at the bottom right corner</li>
      <li>Page number is at the bottom left corner</li>
      <li>Bullet point style rounded bullets</li>
      <li>Aperture Sans is the default standard font for Orbit OS – sleek and modern and also works on all machines</li>
      <li><b>Dark gray</b> is the content font color and <span class="hl-light">light blue</span> is the title color and <span class="hl-bold">bold text color</span></li>
      <li>I have used blue color as default one as most of the corporates choose blue</li>
      <li>Colors can be configured and changed in the master after receiving feedback/ company information from your side</li>
    </ul>
  </div>
  <span class="page-no">1</span>
  <div class="logo-box">Your logo here</div>
</section>

<section class="slide col-1 row-2">
  <h2 class="slide-title">Agenda</h2>
  <svg class="abs" style="left:0;top:0" width="378" height="212" viewBox="0 0 378 212">
    <defs>
      <linearGradient id="screenA" x1="0" y1="0" x2="0" y2="1">
        <stop offset="0" stop-color="#18a6ec"/><stop offset="1" stop-color="#0a72d0"/>
      </linearGradient>
    </defs>
    <g stroke="#bfbfbf" stroke-width="0.5">
      <line x1="125" y1="82" x2="158" y2="82"/><line x1="125" y1="116" x2="158" y2="116"/><line x1="125" y1="151" x2="158" y2="151"/>
      <line x1="220" y1="82" x2="256" y2="82"/><line x1="220" y1="116" x2="256" y2="116"/><line x1="220" y1="151" x2="256" y2="151"/>
    </g>
    <rect x="153" y="44" width="72" height="144" rx="8" fill="#fff" stroke="#c4c4c4" stroke-width="1"/>
    <line x1="185" y1="51" x2="193" y2="51" stroke="#555" stroke-width="0.8"/>
    <circle cx="197" cy="51" r="0.8" fill="#555"/>
    <rect x="159" y="59" width="60" height="113" fill="url(#screenA)"/>
    <circle cx="189" cy="180" r="4.5" fill="none" stroke="#999" stroke-width="0.6"/>
    <g fill="#0c2f80" stroke="#3a8ee0" stroke-width="0.5">
      <circle cx="173" cy="82" r="8"/><circle cx="206" cy="82" r="8"/>
      <circle cx="173" cy="116" r="8"/><circle cx="206" cy="116" r="8"/>
      <circle cx="173" cy="151" r="8"/><circle cx="206" cy="151" r="8"/>
    </g>
    <g fill="none" stroke="#fff" stroke-width="0.6">
      <rect x="170" y="78" width="6" height="8"/>
      <ellipse cx="206" cy="79.5" rx="3.5" ry="1.3"/><path d="M202.5 79.5v5c0 .8 7 .8 7 0v-5M202.5 82c0 .8 7 .8 7 0"/>
      <circle cx="173" cy="116" r="3.5"/><circle cx="173" cy="116" r="1.5"/>
      <path d="M202 118h8a2 2 0 0 0-1-4 3 3 0 0 0-6 1 1.5 1.5 0 0 0-1 3z"/>
      <rect x="170.5" y="147" width="5" height="8" rx="0.6"/>
      <rect x="202" y="148" width="8" height="6"/><path d="M202 148l4 3 4-3"/>
    </g>
  </svg>
  <p class="agenda-item fine" style="left:18px;top:75px">Lorem ipsum dolor sit amet, consectetur adipiscing elit, sed do eiusmod tempor</p>
  <p class="agenda-item fine" style="left:18px;top:109px">Lorem ipsum dolor sit amet, consectetur adipiscing elit, sed do eiusmod tempor</p>
  <p class="agenda-item fine" style="left:18px;top:144px">Lorem ipsum dolor sit amet, consectetur adipiscing elit, sed do eiusmod tempor</p>
  <p class="agenda-item fine" style="left:261px;top:75px">Lorem ipsum dolor sit amet, consectetur adipiscing elit, sed do eiusmod tempor</p>
  <p class="agenda-item fine" style="left:261px;top:109px">Lorem ipsum dolor sit amet, consectetur adipiscing elit, sed do eiusmod tempor</p>
  <p class="agenda-item fine" style="left:261px;top:144px">Lorem ipsum dolor sit amet, consectetur adipiscing elit, sed do eiusmod tempor</p>
  <span class="page-no">2</span>
  <div class="logo-box">Your logo here</div>
</section>

<section class="slide col-2 row-2">
  <div class="photo-fill section-bg" role="img" aria-label="Wireframe satellite dishes glowing on a deep blue starfield"></div>
  <div class="section-title">Section divider page title here</div>
</section>

<section class="slide col-3 row-2">
  <h2 class="slide-title">Agenda</h2>
  <svg class="abs" style="left:0;top:0" width="378" height="212" viewBox="0 0 378 212">
    <defs>
      <linearGradient id="screenB" x1="0" y1="0" x2="0" y2="1">
        <stop offset="0" stop-color="#18a6ec"/><stop offset="1" stop-color="#0a72d0"/>
      </linearGradient>
    </defs>
    <rect x="11" y="70" width="152" height="23" rx="11.5" fill="none" stroke="#1aa3e0" stroke-width="0.8"/>
    <g stroke="#bfbfbf" stroke-width="0.5">
      <line x1="125" y1="116" x2="158" y2="116"/><line x1="125" y1="151" x2="158" y2="151"/>
      <line x1="220" y1="82" x2="256" y2="82"/><line x1="220" y1="116" x2="256" y2="116"/><line x1="220" y1="151" x2="256" y2="151"/>
    </g>
    <rect x="153" y="44" width="72" height="144" rx="8" fill="#fff" stroke="#c4c4c4" stroke-width="1"/>
    <line x1="185" y1="51" x2="193" y2="51" stroke="#555" stroke-width="0.8"/>
    <circle cx="197" cy="51" r="0.8" fill="#555"/>
    <rect x="159" y="59" width="60" height="113" fill="url(#screenB)"/>
    <circle cx="189" cy="180" r="4.5" fill="none" stroke="#999" stroke-width="0.6"/>
    <g fill="#0c2f80" stroke="#3a8ee0" stroke-width="0.5">
      <circle cx="173" cy="82" r="8"/><circle cx="206" cy="82" r="8"/>
      <circle cx="173" cy="116" r="8"/><circle cx="206" cy="116" r="8"/>
      <circle cx="173" cy="151" r="8"/><circle cx="206" cy="151" r="8"/>
    </g>
    <g fill="none" stroke="#fff" stroke-width="0.6">
      <rect x="170" y="78" width="6" height="8"/>
      <ellipse cx="206" cy="79.5" rx="3.5" ry="1.3"/><path d="M202.5 79.5v5c0 .8 7 .8 7 0v-5M202.5 82c0 .8 7 .8 7 0"/>
      <circle cx="173" cy="116" r="3.5"/><circle cx="173" cy="116" r="1.5"/>
      <path d="M202 118h8a2 2 0 0 0-1-4 3 3 0 0 0-6 1 1.5 1.5 0 0 0-1 3z"/>
      <rect x="170.5" y="147" width="5" height="8" rx="0.6"/>
      <rect x="202" y="148" width="8" height="6"/><path d="M202 148l4 3 4-3"/>
    </g>
  </svg>
  <p class="agenda-item fine active" style="left:18px;top:75px">Lorem ipsum dolor sit amet, consectetur adipiscing elit, sed do eiusmod tempor</p>
  <p class="agenda-item fine" style="left:18px;top:109px">Lorem ipsum dolor sit amet, consectetur adipiscing elit, sed do eiusmod tempor</p>
  <p class="agenda-item fine" style="left:18px;top:144px">Lorem ipsum dolor sit amet, consectetur adipiscing elit, sed do eiusmod tempor</p>
  <p class="agenda-item fine" style="left:261px;top:75px">Lorem ipsum dolor sit amet, consectetur adipiscing elit, sed do eiusmod tempor</p>
  <p class="agenda-item fine" style="left:261px;top:109px">Lorem ipsum dolor sit amet, consectetur adipiscing elit, sed do eiusmod tempor</p>
  <p class="agenda-item fine" style="left:261px;top:144px">Lorem ipsum dolor sit amet, consectetur adipiscing elit, sed do eiusmod tempor</p>
  <span class="page-no">3</span>
  <div class="logo-box">Your logo here</div>
</section>

<section class="slide col-1 row-3 impact-bg">
  <h2 class="slide-title on-dark">Impact slide - achievements</h2>
  <div class="stat" style="left:18px;top:58px"><div class="stat-value">$400 M</div><p class="stat-text">Lorem ipsum dolor sit amet, consectetur adipiscing elit, sed do eiusmod tempor</p></div>
  <div class="stat" style="left:100px;top:58px"><div class="stat-value">25+</div><p class="stat-text">Lorem ipsum dolor sit amet, consectetur adipiscing elit, sed do eiusmod tempor</p></div>
  <div class="stat" style="left:18px;top:122px"><div class="stat-value">1500</div><p class="stat-text">Lorem ipsum dolor sit amet, consectetur adipiscing elit, sed do eiusmod tempor</p></div>
  <div class="stat" style="left:100px;top:122px"><div class="stat-value">25+</div><p class="stat-text">Lorem ipsum dolor sit amet, consectetur adipiscing elit, sed do eiusmod tempor</p></div>
  <div class="laptop-screen" role="img" aria-label="Laptop showing a satellite dish against a blurred blue skyline"></div>
  <div class="laptop-base"></div>
  <span class="page-no" style="color:#7cc6f2">3</span>
  <div class="logo-box">Your logo here</div>
</section>

<section class="slide col-2 row-3">
  <h2 class="portfolio-title">Portfolio – image<br>and content</h2>
  <p class="portfolio-text">Some content here in short<br>explaining about the project</p>
  <svg class="abs" style="left:0;top:0" width="378" height="212" viewBox="0 0 378 212">
    <defs>
      <linearGradient id="nodeTech" x1="0" y1="0" x2="1" y2="1"><stop offset="0" stop-color="#0d3a7a"/><stop offset="1" stop-color="#1f9ad0"/></linearGradient>
      <linearGradient id="nodeWarm" x1="0" y1="0" x2="1" y2="1"><stop offset="0" stop-color="#d9c2a8"/><stop offset="1" stop-color="#8a5a44"/></linearGradient>
      <linearGradient id="nodeCity" x1="0" y1="0" x2="1" y2="1"><stop offset="0" stop-color="#6fa6d8"/><stop offset="1" stop-color="#2a5c8c"/></linearGradient>
      <linearGradient id="nodeCool" x1="0" y1="0" x2="1" y2="1"><stop offset="0" stop-color="#e6eef6"/><stop offset="1" stop-color="#7d96b8"/></linearGradient>
      <linearGradient id="phoneShot" x1="0" y1="0" x2="0" y2="1"><stop offset="0" stop-color="#7fa9d6"/><stop offset="1" stop-color="#c7d8ea"/></linearGradient>
    </defs>
    <g stroke="#bdbdbd" stroke-width="0.5">
      <line x1="226" y1="71" x2="226" y2="97"/>
      <line x1="186" y1="92" x2="205" y2="110"/><line x1="274" y1="92" x2="247" y2="110"/>
      <line x1="186" y1="140" x2="205" y2="130"/><line x1="274" y1="140" x2="247" y2="130"/>
    </g>
    <circle cx="226" cy="50" r="21" fill="url(#nodeTech)" role="img" aria-label="Circuit chip photo"/>
    <circle cx="165" cy="84" r="21" fill="url(#nodeWarm)" role="img" aria-label="Hands holding a phone photo"/>
    <circle cx="295" cy="84" r="21" fill="url(#nodeCool)" role="img" aria-label="Card payment photo"/>
    <circle cx="165" cy="147" r="21" fill="url(#nodeCity)" role="img" aria-label="Glass office towers photo"/>
    <circle cx="295" cy="147" r="21" fill="url(#nodeWarm)" role="img" aria-label="Contactless payment photo"/>
    <rect x="205" y="97" width="42" height="84" rx="4" fill="#fff" stroke="#c4c4c4" stroke-width="0.8"/>
    <rect x="208" y="106" width="36" height="65" fill="url(#phoneShot)" role="img" aria-label="Satellite dish photo on phone screen"/>
    <circle cx="226" cy="176" r="2.5" fill="none" stroke="#aaa" stroke-width="0.5"/>
  </svg>
  <p class="node-label" style="left:200px;top:10px">Lorem ipsum dolor sit amet, consectetur adipiscing elit</p>
  <p class="node-label" style="left:139px;top:42px">Lorem ipsum dolor sit amet, consectetur adipiscing elit</p>
  <p class="node-label" style="left:269px;top:43px">Lorem ipsum dolor sit amet, consectetur adipiscing elit</p>
  <p class="node-label" style="left:139px;top:176px">Lorem ipsum dolor sit amet, consectetur adipiscing elit</p>
  <p class="node-label" style="left:269px;top:176px">Lorem ipsum dolor sit amet, consectetur adipiscing elit</p>
  <span class="page-no">4</span>
  <div class="logo-box">Your logo here</div>
</section>

<section class="slide col-3 row-3">
  <h2 class="slide-title">Our growth/<br>Next steps</h2>
  <p class="growth-text">Lorem ipsum dolor sit amet, consectetur adipiscing elit, sed do eiusmod tempor</p>
  <svg class="abs" style="left:0;top:0" width="378" height="212" viewBox="0 0 378 212">
    <defs>
      <linearGradient id="barGrad" x1="0" y1="0" x2="0" y2="1"><stop offset="0" stop-color="#1aa7ee"/><stop offset="1" stop-color="#0a5cc4"/></linearGradient>
    </defs>
    <g fill="url(#barGrad)">
      <path d="M177 74a9 9 0 0 1 18 0V124L175 137H143L177 124z"/>
      <path d="M209 58a9 9 0 0 1 18 0V124L225 137H193L209 124z"/>
      <path d="M241 43a9 9 0 0 1 18 0V124L275 137H243L241 124z"/>
      <path d="M272 27a9 9 0 0 1 18 0V124L325 137H293L272 124z"/>
    </g>
    <g fill="#0b2f80">
      <path d="M143 137h32v8l-16 8-16-8z"/>
      <path d="M193 137h32v8l-16 8-16-8z"/>
      <path d="M243 137h32v8l-16 8-16-8z"/>
      <path d="M293 137h32v8l-16 8-16-8z"/>
    </g>
    <g fill="#fff" stroke="#1aa3e0" stroke-width="0.8">
      <circle cx="186" cy="76" r="7"/><circle cx="218" cy="60" r="7"/>
      <circle cx="250" cy="45" r="7"/><circle cx="281" cy="29" r="7"/>
    </g>
    <g font-family="Open Sans, sans-serif" font-size="6" fill="#0a6fd3" text-anchor="middle">
      <text x="186" y="78.2">1</text><text x="218" y="62.2">2</text><text x="250" y="47.2">3</text><text x="281" y="31.2">4</text>
    </g>
    <g fill="none" stroke="#fff" stroke-width="0.5">
      <rect x="157" y="140" width="4" height="5.5"/>
      <rect x="206" y="141" width="6" height="4.5"/><path d="M206 141l3 2.3 3-2.3"/>
      <path d="M256 145.5h6a1.6 1.6 0 0 0-.8-3 2.3 2.3 0 0 0-4.5.8 1.1 1.1 0 0 0-.7 2.2z"/>
      <ellipse cx="309" cy="141" rx="2.6" ry="1"/><path d="M306.4 141v4c0 .6 5.2 .6 5.2 0v-4"/>
    </g>
  </svg>
  <p class="step-label" style="left:139px;top:162px">Lorem ipsum dolor sit amet, consectetur adipiscing</p>
  <p class="step-label" style="left:189px;top:162px">Lorem ipsum dolor sit amet, consectetur adipiscing</p>
  <p class="step-label" style="left:239px;top:162px">Lorem ipsum dolor sit amet, consectetur adipiscing</p>
  <p class="step-label" style="left:289px;top:162px">Lorem ipsum dolor sit amet, consectetur adipiscing</p>
  <span class="page-no">6</span>
  <div class="logo-box">Your logo here</div>
</section>

<section class="slide col-2 row-4 services-bg">
  <svg class="abs" style="left:0;top:0" width="378" height="212" viewBox="0 0 378 212">
    <path d="M0 0h378v4c-50 2-80 6-95 24-18 22-6 50-44 62-30 10-80-4-120 20-40 24-80 40-119 60z" fill="#0a7fd8"/>
    <path d="M0 0h378c-60 0-105 2-122 20-18 20-4 46-38 58-34 12-74-6-118 18-40 22-70 36-100 50z" fill="var(--navy-deep)"/>
  </svg>
  <h2 class="slide-title on-dark" style="top:16px">Our services</h2>
  <div class="abs" style="left:22px;top:58px;width:130px;height:136px;border-radius:6px;background:linear-gradient(160deg,#d9dde4 0%,#b9c7d8 55%,#7ec34a 100%);opacity:0.9" role="img" aria-label="Illustration of a person at a large phone with a chat bubble, gears and plants"></div>
  <div class="service" style="left:172px;top:102px"><h3>HEADING</h3><p>Lorem ipsum dolor sit amet, consectetur adipiscing elit, sed do eiusmod tempor</p></div>
  <div class="service" style="left:276px;top:102px"><h3>HEADING</h3><p>Lorem ipsum dolor sit amet, consectetur adipiscing elit, sed do eiusmod tempor</p></div>
  <div class="service" style="left:172px;top:149px"><h3>HEADING</h3><p>Lorem ipsum dolor sit amet, consectetur adipiscing elit, sed do eiusmod tempor</p></div>
  <div class="service" style="left:276px;top:149px"><h3>HEADING</h3><p>Lorem ipsum dolor sit amet, consectetur adipiscing elit, sed do eiusmod tempor</p></div>
  <span class="page-no" style="color:#cfe9fb">7</span>
  <div class="logo-box">Your logo here</div>
</section>

</body>
</html>
```